Online shopping portal - Business Card Design

Brightcart.com.au is a complete shopping experience. Search, compare & buy items from partnered stores & receive cashbash for your purchases and referrals.
Mission
Our mission is to provide a system for entrepreneurs to create an ongoing income, while providing consumers worldwide with a better way to shop.
A product brokerage and Internet marketing company that specialises in One-to-One Marketing, Velora Oceania is a subsidiary of Velora Continental Holdings, Inc.
With more than 3 million Preferred Customers and 180,000 Customer Managers worldwide, Velora Continental has generated over $3 billion USD in accumulated retail sales. The Company employs more than 675 people globally with international operations in Australia, United States, Canada, Taiwan, Hong Kong, Mexico & Singapore
Through revolutionary technology and the one-to-one marketing and social shopping Velora Oceania are leveraging the Internet with the power of people to create the economy of the future.
By providing online shoppers with the products and services they want and need — backed by the Company’s people power — Velora Oceania is fast becoming the World Wide Web’s ultimate online shopping destination.
As a result, we are changing the way people shop and changing the economic paradigm where anyone can become financially independent by creating their own economy — Rooted in Goods. Driven by Folks®.
Description
Welcome to a new kind of comparison shopping site where you get PAID cashback to shop!
Simply create an account to start accumulating cash backs each time you make purchases across hundreds of trusted Partner Stores and thousands of your favorite brands through our convenient MonoBag® for one stop shopping.
All merchant stores are backed by BUYNEST.COM's 100% satisfaction guarantee.

Updates
Project Deadline Extended
Reason: Hi all,  I am extending the deadline as i'm going to be away for my birthday (and may not have time to check before the current deadline anyway)  I figure that the more time i give you the better.

Industry/Entity Type
Online Shopping
Contact Information for Business Card
Business Name: Brightcart.com.au
website: www.brightcart.com.au
Friendloop: www.friendloop.com/brightcart.com.au.
Email: info@brightcart.com.au
Phone: Quin on 0438 72 15 94
Requirements
Nice to have
- Create a Brightcart logo

```html
<!DOCTYPE html>
<html lang="en">
<head>
<meta charset="utf-8">
<title>Brightcart.com.au – Business Card Presentation</title>
<link rel="stylesheet" href="https://fonts.googleapis.com/css2?family=Arimo:wght@400;700&family=Open+Sans:wght@400;600;700&display=swap">
<style>
  :root {
    --teal: #2bb8bf;
    --guide: #5cc6cc;
    --crop: #555;
    --paper: #ffffff;
    --card-edge: #cfd6d8;
    --label: #444;
    --rule: #d9d9d9;
    --stage: #4a3f38;
  }
  * { box-sizing: border-box; margin: 0; padding: 0; }
  html, body { width: 829px; height: 1200px; overflow: hidden; background: var(--paper); }
  .sheet { position: relative; width: 829px; height: 1200px; font-family: "Arimo", Arial, sans-serif; }
  .section-label { position: absolute; font-size: 12px; line-height: 14px; color: var(--label); }
  .guides { position: absolute; left: 0; top: 0; }
  .section-rule { position: absolute; left: 76px; top: 625px; width: 690px; height: 1px; background: var(--rule); }

  .card { position: absolute; width: 241px; height: 142px; overflow: hidden; text-align: center; }
  .card--front { background: var(--teal); color: #fff; }
  .card--back { background: var(--paper); border: 1px solid var(--card-edge); color: var(--teal); font-family: "Open Sans", Arial, sans-serif; }

  .brand-mark { display: flex; align-items: center; justify-content: center; gap: 6px; height: 22px; margin-top: 26px; font-weight: 700; font-size: 14px; }
  .brand-mark__dot { width: 20px; height: 20px; border-radius: 50%; }
  .card--front .brand-mark__dot { background: #fff; }
  .card--back .brand-mark { font-family: "Open Sans", Arial, sans-serif; }
  .card--back .brand-mark__dot { background: var(--teal); }

  .card__domain { margin-top: 29px; font-size: 13px; line-height: 15px; font-weight: 700; }
  .features { display: flex; justify-content: center; gap: 18px; margin-top: 12px; }
  .feature { display: flex; flex-direction: column; align-items: center; width: 32px; }
  .feature svg { width: 18px; height: 16px; }
  .feature__label { font-size: 8px; line-height: 10px; font-weight: 700; margin-top: 3px; }

  .card__tagline { margin-top: 28px; font-size: 12px; line-height: 15px; font-weight: 600; }
  .card__details { margin-top: 3px; font-size: 5.2px; font-weight: 600; line-height: 7.2px; }
  .card__phone { margin-top: 3px; font-size: 8.5px; line-height: 11px; font-weight: 700; letter-spacing: 0.3px; }

  .stage { position: absolute; left: 20px; top: 655px; width: 802px; height: 532px; background: var(--stage); }
  .stage .card { transform-origin: 0 0; transform: scale(1.5); }
  .stage .card--back { border-color: #e6e6e6; }
</style>
</head>
<body>
<div class="sheet">

  <div class="section-label" style="left:147px; top:142px;">Alignments</div>

  <svg class="guides" width="829" height="600" aria-hidden="true">
    <g stroke="var(--guide)" stroke-width="1" stroke-dasharray="5 4">
      <line x1="60" y1="219" x2="780" y2="219"/>
      <line x1="60" y1="284" x2="780" y2="284"/>
      <line x1="60" y1="324" x2="780" y2="324"/>
      <line x1="60" y1="400" x2="780" y2="400"/>
      <line x1="240" y1="152" x2="240" y2="572"/>
    </g>
    <g stroke="var(--crop)" stroke-width="0.8">
      <path d="M147 184v9M131 199h9M388 184v9M394 199h9M131 341h9M147 347v9M394 341h9M388 347v9"/>
      <path d="M455 184v9M439 199h9M696 184v9M702 199h9M439 341h9M455 347v9M702 341h9M696 347v9"/>
      <path d="M147 366v9M131 381h9M388 366v9M394 381h9M131 523h9M147 529v9M394 523h9M388 529v9"/>
    </g>
  </svg>

  <div class="card card--front" style="left:147px; top:199px;">
    <div class="brand-mark"><span class="brand-mark__dot"></span>Brightcart</div>
    <div class="card__domain">Brightcart.com.au</div>
    <div class="features">
      <div class="feature">
        <svg viewBox="0 0 18 16"><circle cx="8" cy="7" r="4.5" fill="none" stroke="#fff" stroke-width="2"/><line x1="11.3" y1="10.3" x2="15" y2="14" stroke="#fff" stroke-width="2.4" stroke-linecap="round"/></svg>
        <span class="feature__label">Search</span>
      </div>
      <div class="feature">
        <svg viewBox="0 0 18 16"><path d="M3 5h9l1 10H2z" fill="#fff"/><path d="M5 5V3.5a2.5 2.5 0 0 1 5 0V5" fill="none" stroke="#fff" stroke-width="1.2"/><path d="M10 7h6l1 8h-6z" fill="#fff" opacity=".85"/></svg>
        <span class="feature__label">Compare</span>
      </div>
      <div class="feature">
        <svg viewBox="0 0 18 16"><path d="M1 2h3l2 8h9l2-6H5" fill="none" stroke="#fff" stroke-width="1.6" stroke-linejoin="round"/><circle cx="7" cy="13" r="1.5" fill="#fff"/><circle cx="14" cy="13" r="1.5" fill="#fff"/></svg>
        <span class="feature__label">Buy</span>
      </div>
      <div class="feature">
        <svg viewBox="0 0 18 16"><rect x="2" y="3" width="12" height="9" rx="1" fill="#fff" transform="rotate(-12 8 8)"/><rect x="4" y="5" width="12" height="9" rx="1" fill="#fff" stroke="var(--teal)" stroke-width=".8"/><circle cx="10" cy="9.5" r="2" fill="none" stroke="var(--teal)" stroke-width=".9"/></svg>
        <span class="feature__label">Earn</span>
      </div>
    </div>
  </div>

  <div class="card card--back" style="left:455px; top:199px;">
    <div class="brand-mark"><span class="brand-mark__dot"></span>Brightcart</div>
    <div class="card__tagline">Get paid to shop</div>
    <div class="card__details">Website: www.brightcart.com.au<br>Friendloop: www.friendloop.com/brightcart.com.au.<br>Email: info@brightcart.com.au</div>
    <div class="card__phone">0438 72 15 94</div>
  </div>

  <div class="card card--back" style="left:147px; top:381px;">
    <div class="brand-mark"><span class="brand-mark__dot"></span>Brightcart</div>
    <div class="card__tagline">Get paid to shop</div>
    <div class="card__details">Website: www.brightcart.com.au<br>Friendloop: www.friendloop.com/brightcart.com.au.<br>Email: info@brightcart.com.au</div>
    <div class="card__phone">0438 72 15 94</div>
  </div>

  <div class="section-label" style="left:147px; top:597px;">Art Comp</div>
  <div class="section-rule"></div>

  <div class="stage">
    <div class="card card--front" style="left:25px; top:160px;">
      <div class="brand-mark"><span class="brand-mark__dot"></span>Brightcart</div>
      <div class="card__domain">Brightcart.com.au</div>
      <div class="features">
        <div class="feature">
          <svg viewBox="0 0 18 16"><circle cx="8" cy="7" r="4.5" fill="none" stroke="#fff" stroke-width="2"/><line x1="11.3" y1="10.3" x2="15" y2="14" stroke="#fff" stroke-width="2.4" stroke-linecap="round"/></svg>
          <span class="feature__label">Search</span>
        </div>
        <div class="feature">
          <svg viewBox="0 0 18 16"><path d="M3 5h9l1 10H2z" fill="#fff"/><path d="M5 5V3.5a2.5 2.5 0 0 1 5 0V5" fill="none" stroke="#fff" stroke-width="1.2"/><path d="M10 7h6l1 8h-6z" fill="#fff" opacity=".85"/></svg>
          <span class="feature__label">Compare</span>
        </div>
        <div class="feature">
          <svg viewBox="0 0 18 16"><path d="M1 2h3l2 8h9l2-6H5" fill="none" stroke="#fff" stroke-width="1.6" stroke-linejoin="round"/><circle cx="7" cy="13" r="1.5" fill="#fff"/><circle cx="14" cy="13" r="1.5" fill="#fff"/></svg>
          <span class="feature__label">Buy</span>
        </div>
        <div class="feature">
          <svg viewBox="0 0 18 16"><rect x="2" y="3" width="12" height="9" rx="1" fill="#fff" transform="rotate(-12 8 8)"/><rect x="4" y="5" width="12" height="9" rx="1" fill="#fff" stroke="var(--teal)" stroke-width=".8"/><circle cx="10" cy="9.5" r="2" fill="none" stroke="var(--teal)" stroke-width=".9"/></svg>
          <span class="feature__label">Earn</span>
        </div>
      </div>
    </div>
    <div class="card card--back" style="left:413px; top:160px;">
      <div class="brand-mark"><span class="brand-mark__dot"></span>Brightcart</div>
      <div class="card__tagline">Get paid to shop</div>
      <div class="card__details">Website: www.brightcart.com.au<br>Friendloop: www.friendloop.com/brightcart.com.au.<br>Email: info@brightcart.com.au</div>
      <div class="card__phone">0438 72 15 94</div>
    </div>
  </div>

</div>
</body>
</html>
```